Brava Stone Oven Kitchen (restaurant)

Restaurant with a cool vibe.
We need a refresh of existing site. Appealing to a hip crowd of 25 or older age bracket (mid price to high small town). Constant changes food and cocktail menu. A vibing atmosphere with jazz funk hip music.
Must be able to scale for any device… phone/mobile device super important.
Instagram: @Brava.Linwell
Website: bravalinwell.example

Target Market(s)

25-55 age group

Number of Pages Required

1 page

Font styles to use
Sans Serif

Requirements
Must have
• Simple to navigate. Simplicity is the key to all sophistication.

Links/Buttons
Menu
Gift Cards
Reservations
Take Out
Contact Us
Should not have
• Please, nothing generic looking… no cookie cutter look. Originality

```html
<!DOCTYPE html>
<html lang="en">
<head>
<meta charset="utf-8">
<title>Brava Stone Oven Kitchen</title>
<link href="https://fonts.googleapis.com/css2?family=Outfit:wght@300;400;500;600;700&family=Great+Vibes&family=Fondamento&display=swap" rel="stylesheet">
<style>
:root{
  --green:#0a7d12;
  --ink:#1c1c1c;
  --text:#333;
  --muted:#777;
  --white:#fff;
  --hero-a:#1f3d42;
  --hero-b:#3a3226;
  --footer:#1e2324;
  --footer-line:#3a4244;
  --sketch:#e6e6e6;
}
*{margin:0;padding:0;box-sizing:border-box}
html,body{width:1200px;height:2961px;overflow:hidden;background:var(--white)}
body{position:relative;font-family:"Outfit",sans-serif;color:var(--text)}
.abs{position:absolute}
.script{font-family:"Great Vibes",cursive;font-weight:400}
.center{text-align:center}
.btn{position:absolute;background:var(--green);color:var(--white);display:flex;align-items:center;justify-content:center;font-weight:500;border-radius:3px}
.photo{position:absolute}

/* nav */
.nav{position:absolute;left:0;top:0;width:1200px;height:52px;background:var(--white);border-bottom:1px solid #e3e3e3}
.brand{position:absolute;left:209px;top:8px;font-weight:600;color:var(--ink);font-size:15px;line-height:17px;letter-spacing:.5px}
.nav-links{position:absolute;top:16px;left:450px;display:flex;gap:26px;font-size:14px;color:#555}
.nav-links .active{color:var(--green);text-decoration:underline}
.nav-order{left:873px;top:11px;width:117px;height:29px;border-radius:15px;font-size:14px}

/* hero */
.hero{left:0;top:52px;width:1200px;height:578px;background:linear-gradient(160deg,var(--hero-a) 0%,#24383a 45%,var(--hero-b) 100%)}
.hero-title{left:0;width:1200px;color:var(--white);font-size:58px}
.hero-sub{left:0;width:1200px;color:var(--white);font-size:15px;font-weight:500}
.hero-rule{height:1px;background:var(--white);width:90px;top:403px}

.sketch{position:absolute;border-radius:50%;background:radial-gradient(circle,#f1f1f1 0%,rgba(255,255,255,0) 70%)}

.shadow{box-shadow:0 14px 22px rgba(0,0,0,.25)}
.overline{font-size:14px;color:#555;font-weight:300}
.sub{font-size:16px;color:var(--ink);font-weight:400;line-height:22px}
.para{font-size:12px;color:var(--muted);font-weight:300;line-height:20px}

/* customers */
.avatar{position:absolute;width:74px;height:74px;border-radius:50%;background:linear-gradient(135deg,#5b5550,#2b2826)}
.quote{left:260px;width:680px;font-size:12.5px;color:#666;font-weight:300;line-height:20px}
.cite{left:0;width:1200px;font-size:9.5px;color:#777}
.dot{position:absolute;width:23px;height:23px;border-radius:50%;background:var(--green)}

/* call band */
.band{left:0;top:2361px;width:1200px;height:271px;background:linear-gradient(120deg,#2a3526 0%,#3d3424 40%,#2f2a2b 70%,#1e2a2a 100%)}

/* footer */
.footer{left:0;top:2632px;width:1200px;height:329px;background:var(--footer)}
.f-head{font-size:14px;color:var(--white);font-weight:500;letter-spacing:.3px}
.f-item{font-size:11.5px;color:#d6d6d6;font-weight:300;line-height:15px}
</style>
</head>
<body>

<header class="nav">
  <div class="brand">Brava<br>Stone Oven Kitchen</div>
  <nav class="nav-links">
    <span class="active">Menu</span><span>Gift Cards</span><span>Reservations</span><span>Take Out</span><span>Contact Us</span>
  </nav>
  <div class="btn nav-order">Online Order</div>
</header>

<section>
  <div class="abs hero" role="img" aria-label="Dim restaurant kitchen with stone oven and pizzas in the foreground"></div>
  <h1 class="abs hero-title script center" style="top:206px;line-height:70px">We are one of the best<br>Restaurants</h1>
  <div class="abs hero-sub center" style="top:361px">5-Star Quality</div>
  <div class="abs hero-rule" style="left:400px"></div>
  <div class="abs hero-sub center" style="top:393px">Great Food &nbsp;|&nbsp; Great wine</div>
  <div class="abs hero-rule" style="left:711px"></div>
  <div class="btn" style="left:535px;top:435px;width:130px;height:37px;border-radius:19px;font-size:15px">Order Online</div>
</section>

<div class="sketch" role="img" aria-label="Faint olive branch sketch" style="left:60px;top:630px;width:230px;height:110px"></div>
<div class="sketch" role="img" aria-label="Faint vegetable sketch" style="left:-20px;top:820px;width:110px;height:170px"></div>
<div class="sketch" role="img" aria-label="Faint vegetable sketch" style="left:990px;top:820px;width:120px;height:170px"></div>
<div class="sketch" role="img" aria-label="Faint olive branch sketch" style="left:1120px;top:640px;width:90px;height:90px"></div>

<section>
  <div class="abs overline" style="left:219px;top:722px">Country's Most loved!</div>
  <h2 class="abs script" style="left:219px;top:748px;font-size:38px;color:var(--ink)">Welcome</h2>
  <div class="abs sub" style="left:219px;top:794px;width:230px">A vibing atmosphere with jazz funk hip music.</div>
  <p class="abs para" style="left:219px;top:850px;width:220px">Quisque vel malesuada purus. Nunc in odio eros. Vestibulum convallis, sapien sed mollis vehicula, purus lectus iaculis</p>
  <div class="btn" style="left:220px;top:928px;width:90px;height:30px;font-size:11px">Menu &amp; Order</div>
  <div class="photo" role="img" aria-label="Wood-fired pizzas on a wooden table" style="left:480px;top:703px;width:204px;height:266px;background:linear-gradient(140deg,#c9a070,#8a5a34 55%,#4a3a2c)"></div>
  <div class="photo shadow" role="img" aria-label="Tacos with red cabbage on a dark plate" style="left:720px;top:703px;width:236px;height:266px;background:linear-gradient(150deg,#3c3a36,#5a4f44 50%,#2b2a28)"></div>
  <div class="abs script center" style="left:720px;width:236px;top:852px;font-size:32px;color:var(--white)">Hours</div>
  <div class="abs center" style="left:720px;width:236px;top:902px;font-size:12px;color:var(--white);line-height:17px">Thursday to Sunday<br>12:00pm – 9:00pm</div>
</section>

<div class="sketch" role="img" aria-label="Faint olive branch sketch" style="left:95px;top:1015px;width:210px;height:110px"></div>
<div class="sketch" role="img" aria-label="Faint vegetable sketch" style="left:-10px;top:1210px;width:110px;height:160px"></div>
<div class="sketch" role="img" aria-label="Faint vegetable sketch" style="left:975px;top:1210px;width:130px;height:160px"></div>
<div class="sketch" role="img" aria-label="Faint olive branch sketch" style="left:1100px;top:1020px;width:110px;height:100px"></div>

<section>
  <div class="sketch" role="img" aria-label="Small herb sprig ornament" style="left:390px;top:1062px;width:64px;height:44px"></div>
  <h2 class="abs script center" style="left:208px;width:400px;top:1113px;font-size:38px;color:var(--ink)">Our Restaurant Menu</h2>
  <div class="abs sub center" style="left:208px;width:400px;top:1172px">Quality Ingredients, Tasty Meals</div>
  <p class="abs para center" style="left:240px;width:336px;top:1206px">Quisque vel malesuada purus. Nunc in odio eros. Vestibulum convallis, sapien sed mollis vehicula, purus lectus iaculis neque, quis accumsan arcu.</p>
  <div class="btn" style="left:368px;top:1277px;width:90px;height:29px;font-size:11px">Menu &amp; Order</div>
  <div class="photo shadow" role="img" aria-label="Grilled fish with greens and vegetables" style="left:600px;top:1056px;width:338px;height:262px;background:linear-gradient(160deg,#4b3d2c,#7a6a50 45%,#3a4a2a 80%,#2c2620)"></div>
  <div class="abs center" style="left:600px;width:338px;top:1270px;font-size:14px;color:var(--white)">Good Ingredients I Tasty Meals</div>
</section>

<section>
  <div class="photo shadow" role="img" aria-label="Restaurant interior with open kitchen and wooden counter" style="left:244px;top:1481px;width:337px;height:217px;background:linear-gradient(130deg,#8a8680,#5a4c40 50%,#3a3430)"></div>
  <div class="abs overline" style="left:618px;top:1478px;font-size:13px">Outdoor Dining Hours</div>
  <h2 class="abs script" style="left:618px;top:1500px;font-size:38px;color:var(--ink)">Happy Hours!</h2>
  <div class="abs sub" style="left:618px;top:1556px;width:330px">Quisque vel malesuada purus. Nunc in odio eros malesuada purus</div>
  <p class="abs para" style="left:618px;top:1611px;width:340px">Quisque vel malesuada purus. Nunc in odio eros. Vestibulum convallis, sapien sed mollis vehicula</p>
  <div class="btn" style="left:619px;top:1665px;width:120px;height:30px;font-size:11px">Table Reservations</div>
</section>

<section>
  <div class="sketch" role="img" aria-label="Small herb sprig ornament" style="left:568px;top:1786px;width:64px;height:44px"></div>
  <h2 class="abs center" style="left:0;width:1200px;top:1834px;font-family:'Fondamento',cursive;font-size:29px;font-weight:400;color:var(--ink)">Happy Customers!</h2>
  <div class="avatar" role="img" aria-label="Customer portrait" style="left:563px;top:1907px"></div>
  <p class="abs quote center" style="top:1997px">"Aliquip habitant ea suscipit ea varius cras habitasse ligula doloremque cepteur vehicula iste nibh, mattis assumenda massa"</p>
  <div class="abs cite center" style="top:2051px">- Dana Price</div>
  <div class="avatar" role="img" aria-label="Customer portrait" style="left:563px;top:2080px"></div>
  <p class="abs quote center" style="top:2169px">"Aliquip habitant ea suscipit ea varius cras habitasse ligula doloremque. Fuga reprehenderit quis unde soluta."</p>
  <div class="abs cite center" style="top:2202px">- Marco Ellis</div>
  <div class="abs center" style="left:0;width:1200px;top:2239px;font-size:13px;color:#666;font-weight:300">Check Out Our Reviews</div>
  <span class="dot" style="left:545px;top:2270px"></span>
  <span class="dot" style="left:574px;top:2270px"></span>
  <span class="dot" style="left:603px;top:2270px"></span>
  <span class="dot" style="left:631px;top:2270px"></span>
</section>

<section>
  <div class="abs band" role="img" aria-label="Close-up of tacos with avocado and red onion"></div>
  <div class="abs band" style="background:rgba(0,0,0,.35)"></div>
  <h2 class="abs script center" style="left:0;width:1200px;top:2450px;font-size:36px;color:var(--white)">Call for all your reservations</h2>
  <div class="abs center" style="left:0;width:1200px;top:2510px;font-size:24px;color:var(--white);font-weight:300">555-014-0392</div>
</section>

<footer>
  <div class="abs footer" role="img" aria-label="Dark footer with faint world map"></div>
  <div class="abs center" style="left:209px;width:200px;top:2700px;color:var(--white);font-weight:600;font-size:20px;line-height:22px">Brava<br>Stone Oven Kitchen</div>
  <div class="abs" style="left:232px;top:2774px;width:155px;height:1px;background:var(--footer-line)"></div>
  <div class="abs f-item" style="left:240px;top:2795px;line-height:19px;color:#fff">Thursday to Sunday<br>12:00pm – 8:00pm</div>

  <div class="abs f-head" style="left:480px;top:2693px">HAVE ANY QUESTION</div>
  <svg class="abs" style="left:481px;top:2731px" width="14" height="14" viewBox="0 0 24 24" fill="none" stroke="#0a9d1a" stroke-width="2"><path d="M5 3h4l2 5-3 2a12 12 0 0 0 6 6l2-3 5 2v4a2 2 0 0 1-2 2A18 18 0 0 1 3 5a2 2 0 0 1 2-2z"/></svg>
  <div class="abs f-item" style="left:506px;top:2731px">555-014-0392</div>
  <svg class="abs" style="left:481px;top:2765px" width="14" height="15" viewBox="0 0 24 24" fill="none" stroke="#0a9d1a" stroke-width="2"><path d="M12 22s7-7 7-12a7 7 0 0 0-14 0c0 5 7 12 7 12z"/><circle cx="12" cy="10" r="2.5"/></svg>
  <div class="abs f-item" style="left:506px;top:2764px">48 Linden Avenue<br>Linwell, ON</div>
  <svg class="abs" style="left:481px;top:2817px" width="15" height="13" viewBox="0 0 24 20" fill="none" stroke="#0a9d1a" stroke-width="2"><rect x="2" y="2" width="20" height="16" rx="2"/><path d="M2 4l10 7 10-7"/></svg>
  <div class="abs f-item" style="left:506px;top:2816px">hello@bravalinwell.example</div>

  <div class="abs f-head" style="left:737px;top:2693px">INFO</div>
  <div class="abs f-item" style="left:737px;top:2731px;line-height:21.2px">Home<br>Gift Cards<br>Reservations<br>Take Out<br>Contact Us<br>Online Order</div>

  <div class="abs f-head" style="left:898px;top:2693px">SOCIAL</div>
  <span class="dot" style="left:902px;top:2771px;width:24px;height:24px"></span>
  <span class="dot" style="left:932px;top:2771px;width:24px;height:24px"></span>
  <span class="dot" style="left:962px;top:2771px;width:24px;height:24px"></span>

  <div class="abs" style="left:0;top:2892px;width:1200px;height:1px;background:var(--footer-line)"></div>
  <div class="abs" style="left:219px;top:2917px;font-size:10.5px;color:#ccc;font-weight:300">© 2021 <span style="color:#0a9d1a">Brava</span>. All Rights Reserved.</div>
  <div class="abs" style="left:829px;top:2917px;font-size:10.5px;color:#ccc;font-weight:300">Privacy Policy &nbsp;&nbsp;| &nbsp;&nbsp;Terms of Use</div>
</footer>

</body>
</html>
```